Specialized instructional design consultant needs a business card

**Hi Designers,
This project is put on hold until the logo project is completed. We will re-open this project at that time, if you are interested in the logo project see following link
http://jobs.gridmarketo.com/job.aspx?id=517203

I need a business card that makes me stand out as an innovative, specialized professional that organizations can trust to lead their team through a project. I develop customized learning for the workflow - so my work is about being able to connect with my clients and their teams quickly and build their trust so we can develop the right solution. I like primary colours, designs that represent connections and movement. The final design should be clean, concise ... and cool.

Here are the details:

Company name is in the logo

Helen Marwick, B.Sc., M.Ed., PMP
helen.marwick@quillfern.com

Peter Marwick, MBA
peter.marwick@quillfern.com

Location:
Larkmoor, Westhaven Province
Northreach

Phone:
250.471.3085

Reason: I needed to delay the start of this project because my logo wasn't done. Now it is done so we can move forward.

Target Market(s)

Executives who have the authority to make decisions about whether or not to hire me as a consultant on their team

Industry/Entity Type

Business

Font styles to use
Sans Serif

Requirements
Must have
• Clean, concise, but stands out
keep it simple
depicts connections between individual parts
primary colours
Nice to have
• a sense of movement / flow

```html
<!DOCTYPE html>
<html lang="en">
<head>
<meta charset="UTF-8">
<title>Quillfern Consulting – Business Card</title>
<link rel="stylesheet" href="https://fonts.googleapis.com/css2?family=Open+Sans:wght@400;600;700&display=swap">
<style>
  :root {
    --page: #e4e3e1;
    --card: #ffffff;
    --card-shade: #f0f0f0;
    --orange: #e8952c;
    --red: #8e1a10;
    --ink: #3b3b3b;
    --brand: #6e6e6e;
    --name: #7a1410;
  }
  * { box-sizing: border-box; margin: 0; padding: 0; }
  html, body {
    width: 1200px;
    height: 871px;
    overflow: hidden;
    background: var(--page);
    font-family: "Open Sans", Arial, sans-serif;
  }
  .sheet {
    width: 1200px;
    height: 871px;
    display: flex;
    align-items: center;
    justify-content: center;
    gap: 40px;
  }
  .card {
    position: relative;
    width: 560px;
    height: 320px;
    background: linear-gradient(160deg, var(--card) 0%, var(--card) 55%, var(--card-shade) 100%);
    box-shadow: 0 10px 28px rgba(0,0,0,0.18);
    overflow: hidden;
  }
  .card-art {
    position: absolute;
    inset: 0;
    width: 100%;
    height: 100%;
  }
  .brand {
    position: absolute;
    top: 62px;
    right: 48px;
    display: flex;
    align-items: center;
    gap: 12px;
  }
  .brand-dot {
    width: 22px;
    height: 22px;
    border-radius: 50%;
    background: var(--orange);
  }
  .brand-name {
    font-size: 30px;
    font-weight: 600;
    color: var(--brand);
    letter-spacing: 0.5px;
    line-height: 1;
  }
  .contact {
    position: absolute;
    top: 44px;
    right: 40px;
    text-align: right;
    color: var(--ink);
    font-size: 14px;
    line-height: 1.45;
    letter-spacing: 0.6px;
  }
  .contact-name {
    font-size: 20px;
    font-weight: 700;
    color: var(--name);
    letter-spacing: 0.8px;
    margin-bottom: 10px;
  }
  .contact-location { margin-bottom: 10px; }
  .contact-line {
    display: flex;
    justify-content: flex-end;
    align-items: center;
    gap: 8px;
  }
  .contact-icon { width: 14px; height: 14px; flex: none; }
</style>
</head>
<body>
<main class="sheet">

  <section class="card card-front" aria-label="Card front">
    <svg class="card-art" viewBox="0 0 560 320" aria-hidden="true">
      <line x1="0" y1="236" x2="560" y2="214" stroke="var(--orange)" stroke-width="2"/>
      <polygon points="0,268 560,250 560,274 0,292" fill="var(--red)"/>
    </svg>
    <div class="brand">
      <span class="brand-dot"></span>
      <span class="brand-name">Quillfern Consulting</span>
    </div>
  </section>

  <section class="card card-back" aria-label="Card back">
    <svg class="card-art" viewBox="0 0 560 320" aria-hidden="true">
      <line x1="0" y1="236" x2="560" y2="214" stroke="var(--orange)" stroke-width="2"/>
      <polygon points="0,268 560,250 560,274 0,292" fill="var(--red)"/>
    </svg>
    <div class="contact">
      <p class="contact-name">Peter Marwick, MBA</p>
      <p class="contact-location">Location<br>Larkmoor, Westhaven Province<br>Northreach</p>
      <p class="contact-line">250.471.3085
        <svg class="contact-icon" viewBox="0 0 16 16" aria-hidden="true"><path d="M3 2h3l1.5 3.5-2 1.2a9 9 0 0 0 3.8 3.8l1.2-2L14 10v3c0 .6-.4 1-1 1A11 11 0 0 1 2 3c0-.6.4-1 1-1z" fill="var(--orange)"/></svg>
      </p>
      <p class="contact-line">peter.marwick@quillfern.com
        <svg class="contact-icon" viewBox="0 0 16 16" aria-hidden="true"><rect x="1.5" y="3.5" width="13" height="9" fill="none" stroke="var(--orange)" stroke-width="1.5"/><path d="M1.5 3.5 8 9l6.5-5.5" fill="none" stroke="var(--orange)" stroke-width="1.5"/></svg>
      </p>
    </div>
  </section>

</main>
</body>
</html>
```